New Website for novelty yarn producer

We need a new website for our company, Tarvek. We make highly tailored yarns for weavers worldwide. This year marks our 40th anniversary and we want to evolve our image and identity.

Our temporary website can be found at:
www.tarvekyarns.com

Our only concern in that throughout the website the protagonist must be our client, we make their creations possible and are highly adaptable both during the ideation process of the yarn as well as in the production. This is at the core of the way we do business and is summarised within the concept of FPM (Fluid Partner Method).

Industry/Entity Type

Textile

Number of Pages Required

1 page

Colors
9bcb3c

Requirements
Must have
• Fluid Partner Method (FPM) - can be found on or current website www.tarvekyarns.com

```html
<!DOCTYPE html>
<html lang="en">
<head>
<meta charset="utf-8">
<title>Tarvek – Tailored Weaving Solutions</title>
<link href="https://fonts.googleapis.com/css2?family=Open+Sans:wght@300;400;600;700&display=swap" rel="stylesheet">
<style>
:root{
  --green:#9bcb3c;
  --green-dark:#86b42c;
  --ink:#333;
  --muted:#8a8a8a;
  --blue-text:#3b5a78;
  --dark:#2b2b2b;
  --darker:#222;
  --band-dark:#262626;
  --light:#f0f0f0;
  --white:#fff;
}
*{box-sizing:border-box;margin:0;padding:0}
html,body{width:679px;height:1200px;overflow:hidden}
body{font-family:"Open Sans",sans-serif;color:var(--ink);background:var(--white);position:relative}

.site-header{position:absolute;top:0;left:0;width:679px;height:34px;background:rgba(255,255,255,.96);display:flex;align-items:center;justify-content:space-between;padding:0 18px;z-index:2}
.brand{font-weight:700;font-size:17px;letter-spacing:1px;color:var(--dark);display:flex;align-items:center;gap:6px}
.brand-dot{width:8px;height:8px;background:var(--green);border-radius:50%}
.main-nav{display:flex;gap:2px;font-size:6.5px}
.main-nav a{color:var(--ink);text-decoration:none;padding:4px 6px}
.main-nav a.active{background:var(--green);color:var(--white)}

.hero{position:absolute;top:0;left:0;width:679px;height:340px}
.hero-photo{position:absolute;inset:0;background:
  radial-gradient(circle at 15% 30%,#d8a23a 0,transparent 22%),
  radial-gradient(circle at 30% 75%,#c0264a 0,transparent 25%),
  radial-gradient(circle at 55% 20%,#e33c3c 0,transparent 22%),
  radial-gradient(circle at 80% 35%,#f0a51f 0,transparent 22%),
  radial-gradient(circle at 88% 80%,#6a3fa0 0,transparent 25%),
  radial-gradient(circle at 60% 85%,#2f8fb0 0,transparent 25%),
  radial-gradient(circle at 5% 85%,#7a4bb0 0,transparent 22%),
  linear-gradient(135deg,#7a2d6b,#b8323c 50%,#3a6f9c)}
.hero-shade{position:absolute;inset:0;background:radial-gradient(ellipse at 50% 70%,rgba(0,0,0,.45),rgba(0,0,0,.1) 60%)}
.hero-badge{position:absolute;left:316px;top:210px;width:48px;height:48px;border:2px solid var(--white);border-radius:50%;color:var(--white);text-align:center;padding-top:7px}
.hero-badge b{display:block;font-size:17px;line-height:18px;font-weight:600}
.hero-badge span{font-size:5px;letter-spacing:1px}
.hero-title{position:absolute;top:280px;width:100%;text-align:center;color:var(--white);font-size:22px;font-weight:600;text-shadow:0 1px 4px rgba(0,0,0,.4)}
.hero-arrow{position:absolute;top:186px;width:14px;height:18px;background:rgba(0,0,0,.4);display:flex;align-items:center;justify-content:center}
.hero-arrow.prev{left:0}.hero-arrow.next{right:0}

.features{position:absolute;top:362px;left:0;width:679px;display:flex;justify-content:center;gap:36px}
.feature{width:170px;text-align:center}
.feature svg{height:30px;width:40px}
.feature h3{color:var(--green);font-weight:400;font-size:14px;margin:6px 0 5px}
.feature p{font-size:5.5px;line-height:1.6;color:var(--muted)}

.method-band{position:absolute;top:540px;left:0;width:679px;height:205px;display:flex}
.thread-photo{width:310px;height:100%;background:linear-gradient(160deg,#e7c6a0,#c2413e 35%,#d9d2c4 55%,#7a6fa0 75%,#e0a46a)}
.method-panel{flex:1;background:var(--band-dark);padding:36px 0 0 22px;color:#cfcfcf}
.method-mark{display:flex;align-items:center;gap:8px;color:var(--white);font-size:9px;letter-spacing:1px;line-height:1.3;text-transform:uppercase}
.method-mark i{width:30px;height:30px;border:3px solid var(--green);border-radius:50%}
.method-panel h4{color:var(--green);font-weight:400;font-size:8px;margin:14px 0 6px}
.method-panel p{font-size:5.5px;line-height:1.6;width:230px;color:#aaa}
.btn{display:inline-block;background:var(--green);color:var(--white);font-size:7px;font-weight:600;text-transform:uppercase;padding:6px 12px;text-decoration:none}
.method-panel .btn{margin-top:12px}

.about{position:absolute;top:775px;left:0;width:679px;text-align:center;color:var(--blue-text);font-size:8.5px;line-height:1.6;font-weight:600}
.about p{width:520px;margin:0 auto 14px}
.about .btn{margin-top:2px}

.stats{position:absolute;top:945px;left:0;width:679px;height:118px;background:var(--light);display:flex;justify-content:center;gap:110px;padding-top:28px;text-align:center}
.stat b{display:block;font-size:30px;font-weight:600;color:var(--dark);line-height:1}
.stat span{font-size:6.5px;text-transform:uppercase;letter-spacing:.5px}

.site-footer{position:absolute;top:1063px;left:0;width:679px;height:115px;background:var(--dark);color:#aaa;display:flex;padding:18px 0 0 70px;gap:60px}
.footer-col h5{color:var(--white);font-size:8px;font-weight:600;margin-bottom:8px}
.footer-col li{list-style:none;font-size:5.5px;line-height:2;display:flex;align-items:center;gap:4px}
.footer-col li::before{content:"";width:3px;height:3px;background:var(--green);border-radius:50%}
.links-list{display:grid;grid-template-columns:80px 50px}
.bottom-bar{position:absolute;top:1178px;left:0;width:679px;height:22px;background:var(--darker);color:#888;font-size:5px;display:flex;align-items:center;justify-content:space-between;padding:0 40px 0 70px}
.socials{display:flex;gap:4px}
.socials i{width:10px;height:10px;border-radius:50%;background:#3b5998}
.socials i+i{background:#2aa0d8}
</style>
</head>
<body>

<header class="site-header">
  <div class="brand"><span class="brand-dot"></span>TARVEK</div>
  <nav class="main-nav">
    <a class="active" href="#">Home</a><a href="#">About</a><a href="#">Fluid Partner Method</a><a href="#">Heritage</a><a href="#">Team</a><a href="#">Blog</a><a href="#">Contact</a>
  </nav>
</header>

<section class="hero">
  <div class="hero-photo" role="img" aria-label="Close-up of colourful balls of yarn in red, orange, purple and blue"></div>
  <div class="hero-shade"></div>
  <div class="hero-badge"><b>40</b><span>YEARS</span></div>
  <h1 class="hero-title">Tailored Weaving Solutions</h1>
  <div class="hero-arrow prev"><svg width="5" height="8"><path d="M4 0L0 4l4 4" stroke="#fff" fill="none"/></svg></div>
  <div class="hero-arrow next"><svg width="5" height="8"><path d="M1 0l4 4-4 4" stroke="#fff" fill="none"/></svg></div>
</section>

<section class="features">
  <article class="feature">
    <svg viewBox="0 0 40 30" fill="none" stroke="#9bcb3c" stroke-width="1.5"><path d="M8 26l4-20h4l4 20zM20 26l4-20h4l4 20z"/><path d="M4 28h32"/></svg>
    <h3>Experience</h3>
    <p>Over forty years our company has gathered the knowledge and skills that define the quality of every yarn we deliver to weavers.</p>
  </article>
  <article class="feature">
    <svg viewBox="0 0 40 30" fill="none" stroke="#9bcb3c" stroke-width="1.5"><path d="M20 5a8 8 0 0 0-5 14v4h10v-4a8 8 0 0 0-5-14zM16 26h8M20 0v2M8 8l2 1M32 8l-2 1"/></svg>
    <h3>Creativity</h3>
    <p>Our belief is that the key to success is a constant flow of ideas, curiosity and openness to new materials, colours and effects for every client.</p>
  </article>
  <article class="feature">
    <svg viewBox="0 0 40 30" fill="none" stroke="#9bcb3c" stroke-width="1.5"><circle cx="20" cy="15" r="11"/><path d="M11 9c6 2 12 8 14 16M14 24c0-7 6-14 15-15M9 16c6 0 12 4 15 10"/></svg>
    <h3>Professionality</h3>
    <p>We are a trusted partner at every step, from first sample to final delivery, keeping quality, timing and care at the centre.</p>
  </article>
</section>

<section class="method-band">
  <div class="thread-photo" role="img" aria-label="Diagonal rows of multicoloured warp threads"></div>
  <div class="method-panel">
    <div class="method-mark"><i></i><span>Fluid<br>Partner<br>Method</span></div>
    <h4>Production built around you</h4>
    <p>Flexibility and close dialogue make every project unique, from the first idea to the finished cone shipped to you.</p>
    <a class="btn" href="#">Find out more</a>
  </div>
</section>

<section class="about">
  <p>Our team has decades of experience in providing yarn solutions to weavers around the world, assisting them in the creation of outstanding textiles.</p>
  <p>Our clients can expect open lines of communication, clarity and professionalism.</p>
  <p>Our focus is our client.<br>The success of a client is our success.</p>
  <a class="btn" href="#">Our heritage</a>
</section>

<section class="stats">
  <div class="stat"><b>40</b><span>Years in business</span></div>
  <div class="stat"><b>2</b><span>Million kilograms/yr</span></div>
  <div class="stat"><b>8</b><span>Brands</span></div>
</section>

<footer class="site-footer">
  <div class="footer-col">
    <h5>Contact Info</h5>
    <ul><li>Via dei Filati 18, 24020 Gorle, Italy</li><li>Tel +39 035 000 1122</li><li>Fax +39 035 000 1133</li><li>info@tarvekyarns.com</li></ul>
  </div>
  <div class="footer-col">
    <h5>More Details</h5>
    <ul><li>VAT IT 01234567890</li><li>Share capital € 500.000</li><li>Registered Bergamo 012345</li></ul>
  </div>
  <div class="footer-col">
    <h5>Links</h5>
    <ul class="links-list"><li>Home</li><li>Team</li><li>About</li><li>Blog</li><li>Fluid Partner Method</li><li>Contact</li><li>Heritage</li></ul>
  </div>
</footer>
<div class="bottom-bar">
  <span>Copyright © 2016 - Tarvek Yarns srl. All rights reserved.</span>
  <div class="socials"><i></i><i></i></div>
</div>

</body>
</html>
```